Titelseite und Rückseite für Schraubenkatalog gesucht
Zielgruppe
KOR Fügesysteme GmbH verkauft Schrauben, Werkzeuge, Industriebedarf,Betriebsausstattung, Arbeitsschutz, an große und kleine Firmen.
Für einen Schraubenkatalog soll die Titel Seite und die Rückseite gestaltet werden, Größe A4
Kontaktdaten auf der Webseite www.kor-Fuegesysteme.de
Der Wunsch des Kunden ist es soll sehr hochwertig, edel aussehen.
Das Logo und natürlich die Kontaktdaten sollen mit drauf sein.
Aufgabenstellung
Vielleicht eine Schraube oder Mutter oder........
Der Spruch: Wir halten zusammen, was zusammen gehört.' soll mit eingebaut werden
Wir werden gegen Abend alle Vorschläge bewerten nach Absprache mit dem Kunden.
Vielen Dank für Ihre Vorschläge schon mal.

```html
<!DOCTYPE html>
<html lang="de">
<head>
<meta charset="utf-8">
<title>KOR Fügesysteme GmbH – Katalog Titel- und Rückseite</title>
<link href="https://fonts.googleapis.com/css2?family=Open+Sans:wght@400;700&family=Teko:wght@500&display=swap" rel="stylesheet">
<style>
  :root {
    --backdrop: #4a5052;
    --cover-deep: #1f4558;
    --cover-mid: #3f6e85;
    --cover-light: #8fb0c0;
    --brand-red: #e0262a;
    --text-light: #eef3f6;
    --text-muted: #9aa7ae;
    --steel: #aab4ba;
  }
  * { box-sizing: border-box; margin: 0; padding: 0; }
  html, body { width: 1200px; height: 796px; overflow: hidden; }
  body {
    background: var(--backdrop);
    font-family: "Open Sans", Arial, sans-serif;
    position: relative;
  }
  .cover {
    position: absolute;
    top: 130px;
    width: 380px;
    height: 537px;
    overflow: hidden;
    color: var(--text-light);
    background:
      radial-gradient(ellipse at 40% 35%, var(--cover-light) 0%, transparent 55%),
      linear-gradient(160deg, var(--cover-mid) 0%, var(--cover-deep) 100%);
    box-shadow: 0 12px 30px rgba(0,0,0,.45);
  }
  .cover--front { left: 190px; }
  .cover--back { left: 630px; }

  .brand {
    position: absolute;
    text-align: center;
    width: 190px;
  }
  .brand__name {
    color: var(--brand-red);
    font-weight: 700;
    font-size: 15px;
    letter-spacing: .5px;
    text-transform: uppercase;
    white-space: nowrap;
  }
  .brand__legal {
    display: flex;
    align-items: center;
    gap: 6px;
    margin-top: 2px;
    font-size: 9px;
    font-weight: 700;
    letter-spacing: 1px;
    color: var(--text-light);
  }
  .brand__legal::before, .brand__legal::after {
    content: "";
    flex: 1;
    height: 1px;
    background: var(--text-light);
  }
  .brand__mark {
    width: 14px; height: 14px;
    background: var(--brand-red);
    margin: 0 auto 6px;
  }
  .cover--front .brand { top: 28px; right: 14px; }
  .cover--back .brand { bottom: 70px; right: 30px; }

  .product-photo {
    position: absolute;
    border-radius: 6px;
    background: radial-gradient(ellipse at 50% 45%, #c9d1d5 0%, #7f8f98 45%, rgba(63,110,133,0) 75%);
  }
  .cover--front .product-photo { left: 50px; top: 95px; width: 290px; height: 300px; }
  .cover--back .product-photo {
    left: 110px; top: 200px; width: 200px; height: 230px;
    opacity: .45;
  }

  .slogan {
    position: absolute;
    left: 30px; right: 28px; top: 400px;
    font-family: "Teko", "Arial Narrow", sans-serif;
    font-weight: 500;
    font-size: 34px;
    line-height: 32px;
    text-transform: uppercase;
    letter-spacing: 1px;
  }
  .slogan span { display: block; }
  .slogan span + span { text-align: right; }
  .catalog-label {
    position: absolute;
    bottom: 8px; left: 0; right: 0;
    text-align: center;
    font-weight: 700;
    font-size: 12px;
    color: var(--text-muted);
    letter-spacing: .5px;
  }

  .contact {
    position: absolute;
    left: 28px; top: 48px; right: 20px;
    font-size: 10.5px;
    line-height: 17px;
  }
  .contact__title {
    font-family: "Teko", "Arial Narrow", sans-serif;
    font-weight: 500;
    font-size: 22px;
    line-height: 24px;
    text-transform: uppercase;
    letter-spacing: .5px;
    margin-bottom: 8px;
  }
</style>
</head>
<body>
  <section class="cover cover--front" aria-label="Titelseite">
    <div class="brand">
      <div class="brand__mark"></div>
      <div class="brand__name">KOR Fügesysteme</div>
      <div class="brand__legal">GMBH</div>
    </div>
    <div class="product-photo" role="img" aria-label="Foto: Gelenkkopfschraube mit Mutter und eine Sechskantmutter mit Gewindestück aus Edelstahl"></div>
    <h1 class="slogan">
      <span>Wir halten zusammen,</span>
      <span>was zusammen gehört</span>
    </h1>
    <p class="catalog-label">Katalogsortiment</p>
  </section>

  <section class="cover cover--back" aria-label="Rückseite">
    <div class="contact">
      <h2 class="contact__title">KOR Fügesysteme GmbH</h2>
      <p>Ihr neuer Verbindungspartner in und um Talbrück.</p>
      <p>Wir würden uns freuen, wenn Sie sich jetzt schon vertrauensvoll</p>
      <p>an uns wenden.</p>
      <p>+49 (0) 123 45678901</p>
      <p>+49 (0) 123 45678902</p>
      <p>info@kor-fuegesysteme.de</p>
    </div>
    <div class="product-photo" role="img" aria-label="Foto: zwei Flanschschrauben aus Stahl, blass in den Hintergrund gelegt"></div>
    <div class="brand">
      <div class="brand__mark"></div>
      <div class="brand__name">KOR Fügesysteme</div>
      <div class="brand__legal">GMBH</div>
    </div>
  </section>
</body>
</html>
```